Keep Harbor Homes. Avoid short sale, foreclosure, repossession, negative credit inquires and all other negative actions associated with your real estate.

Call 844-27-LUMEN or info@keepharborhomes.example

```html
<!DOCTYPE html>
<html lang="en">
<head>
<meta charset="utf-8">
<title>Keep Harbor Homes – Poster</title>
<link rel="stylesheet" href="https://fonts.googleapis.com/css2?family=Didact+Gothic&family=Arimo:wght@400;700&display=swap">
<style>
  :root {
    --backdrop: #d9d9d7;
    --paper: #eceeee;
    --charcoal: #2b2b2b;
    --signal-red: #e31e24;
    --slate: #a0a1a1;
    --white: #ffffff;
    --art-light: #e6e8e8;
    --art-mid: #d6d8d8;
  }
  * { box-sizing: border-box; margin: 0; padding: 0; }
  html, body {
    width: 891px;
    height: 1200px;
    overflow: hidden;
    background: var(--backdrop);
  }
  .poster {
    position: absolute;
    left: 59px;
    top: 32px;
    width: 773px;
    height: 1135px;
    background: var(--paper);
    display: flex;
    flex-direction: column;
    box-shadow: 0 2px 10px rgba(0,0,0,0.15);
  }
  .hero {
    position: relative;
    height: 439px;
    background: var(--paper);
  }
  .hero-art {
    position: absolute;
    left: 66px;
    top: 120px;
    width: 640px;
    height: 319px;
    background: linear-gradient(180deg, var(--art-light) 0%, var(--art-mid) 100%);
    border-radius: 4px 4px 0 0;
  }
  .brand-line {
    display: flex;
    align-items: center;
    justify-content: center;
    color: var(--white);
    font-family: "Didact Gothic", sans-serif;
    text-transform: uppercase;
    white-space: nowrap;
  }
  .brand-line--top {
    height: 150px;
    background: var(--charcoal);
    font-size: 74px;
    letter-spacing: 2px;
  }
  .brand-line--bottom {
    height: 106px;
    background: var(--signal-red);
    font-size: 92px;
    letter-spacing: 8px;
    line-height: 1;
  }
  .services {
    height: 313px;
    background: var(--slate);
    display: flex;
    justify-content: center;
    padding-top: 26px;
  }
  .services p {
    width: 540px;
    color: var(--white);
    font-family: "Arimo", Arial, sans-serif;
    font-size: 26px;
    line-height: 59px;
    text-align: justify;
    text-align-last: center;
    text-transform: uppercase;
  }
  .contact {
    height: 127px;
    background: var(--signal-red);
    color: var(--white);
    font-family: "Arimo", Arial, sans-serif;
    text-align: center;
    padding-top: 10px;
  }
  .contact-phone {
    display: block;
    font-size: 58px;
    font-weight: 700;
    line-height: 64px;
  }
  .contact-email {
    display: block;
    font-size: 26px;
    line-height: 32px;
  }
</style>
</head>
<body>
  <main class="poster">
    <section class="hero">
      <div class="hero-art" role="img" aria-label="Illustration of a seesaw balancing a dollar coin against a house"></div>
    </section>
    <h1>
      <span class="brand-line brand-line--top">Keep Harbor</span>
      <span class="brand-line brand-line--bottom">Homes</span>
    </h1>
    <section class="services">
      <p>Avoid short sale, foreclosure, repossession, negative credit inquires and all other negative actions associated with your real estate.</p>
    </section>
    <footer class="contact">
      <span class="contact-phone">844-27-LUMEN</span>
      <span class="contact-email">info@keepharborhomes.example</span>
    </footer>
  </main>
</body>
</html>
```